International Energy supply analytics vendor requires a flyer designed

We, Tol power are a startup. we have build an energy supply analytics software called RPT. now we want power generators ( wind power generator , solar power generator, hydro power generator ) (renewable energy generators) to try out our trial version for free.

The trial version has a time span of 2 years.

since this is enterprise software, the end user has to be really comfortable about using RPT.

we have a website ( www.tolpowerhub.net) where we introduce
Tol power and RPT.

we want a flyer that introduces RPT and informs about the trial version and period

The design should convey energy industry veteran, growth and problem solving

the colors are left to you

the flyer should mention the website ( www.tolpowerhub.net)
Updates

Hi guys

I have edited my web page 'www.tolpowerhub.net' and made it more bold and aggressive. I am challenging the status quo. 
from introducing Tol power as an energy supply analytics company, i want to hit it right on the head stating the problem. 

the problem statement is " how good is your power forecast".. are you satisfied. RPT the product of Tol power , takes the power forecast, works on it , using historical data and provides a better estimate of the forecast. 

I think the flyer which can be maximum 2 pages needs to do that. you can show pictures of wind turbines ( the wind industry is my customer), a dam as (hydro energy is also a customer ) 

 I have uploaded a picture of the spreadsheet which i do show on my webpage. 

the spreadsheet shows the depth of the problem and the current quick fix that the industry has taken to.

please do not forget to add the contact information and mention the two year trial version.

We are looking for early adopters.

thanx

Dinesh

 

I had written in my update :

. RPT the product of Tol power , takes the power forecast, works on it , using historical data and provides a better estimate of the forecast. 

it should read

. RPT the product of Tol power , takes the current  power forecast ,historical forecast data, historical actual generation data as inputs, crunches the numbers and provides a better probabilistic estimate of Day Ahead Bids . 

Target Market(s)

corporate end users, wind power generators, hydro power generators,

Industry/Entity Type

Software

```html
<!DOCTYPE html>
<html lang="en">
<head>
<meta charset="utf-8">
<title>RPT – Power Forecast Flyer</title>
<link rel="stylesheet" href="https://fonts.googleapis.com/css2?family=Arimo:wght@400;700&family=Tinos:wght@400;700&display=swap">
<style>
  :root {
    --stage: #3a3a3d;
    --paper-top: #f2e8d2;
    --paper-bottom: #e4d3ae;
    --ink: #2a2622;
    --accent-red: #d8262b;
    --frame: #0d0d0d;
    --col-white: #ffffff;
    --col-lilac: #e9def1;
    --col-violet: #cdbbe2;
    --col-sky: #c4e6f6;
    --col-blue: #9ccfee;
    --header-blue: #2b2fa8;
  }
  * { box-sizing: border-box; margin: 0; padding: 0; }
  html, body { width: 1200px; height: 900px; overflow: hidden; }
  body {
    background: var(--stage);
    font-family: "Arimo", Arial, sans-serif;
    color: var(--ink);
    position: relative;
  }
  .flyer {
    position: absolute;
    left: 270px; top: 24px;
    width: 660px; height: 852px;
    background: linear-gradient(180deg, var(--paper-top), var(--paper-bottom));
    padding: 34px 44px 0;
  }
  .edge-band { position: absolute; background: var(--frame); }
  .edge-band--left { left: -10px; top: 70px; width: 16px; height: 190px; }
  .edge-band--right { right: -10px; top: 0; width: 16px; height: 150px; }
  .intro {
    font-size: 16px; line-height: 1.3; text-align: center;
    padding: 0 50px;
  }
  .section-title {
    margin-top: 10px;
    color: var(--accent-red);
    font-size: 22px; font-weight: 400; text-align: center;
  }
  .forecast-frame {
    margin-top: 10px;
    border: 8px solid var(--frame);
    background: linear-gradient(90deg, var(--col-white) 0%, var(--col-white) 22%, var(--col-lilac) 38%, var(--col-violet) 55%, var(--col-sky) 72%, var(--col-blue) 100%);
    padding: 6px 10px 8px;
  }
  .forecast-table {
    width: 100%; border-collapse: collapse;
    font-family: "Tinos", "Times New Roman", serif;
    font-size: 11px; line-height: 1.3;
  }
  .forecast-table th {
    color: var(--header-blue); font-weight: 700; font-size: 10px; line-height: 1.2;
    text-align: left; vertical-align: bottom; padding: 0 4px 3px;
  }
  .forecast-table td { padding: 0 4px; text-align: right; white-space: nowrap; }
  .forecast-table td.date { text-align: left; }
  .forecast-table td.alert { color: var(--accent-red); }
  .explainer {
    margin-top: 12px;
    font-size: 14px; line-height: 1.3; text-align: center; padding: 0 16px;
  }
  .offer { position: relative; margin-top: 16px; height: 300px; }
  .dam-photo {
    position: absolute; left: 0; top: 70px;
    width: 170px; height: 118px;
    border: 7px solid var(--frame);
    background: linear-gradient(160deg, #9fb6c8 0%, #dfe8ee 45%, #6f7f8a 100%);
  }
  .offer-copy {
    position: absolute; left: 186px; right: 96px; top: 0;
    font-size: 14px; line-height: 1.3; text-align: center;
  }
  .offer-copy .highlight { color: var(--accent-red); }
  .trial-span {
    color: var(--accent-red); font-size: 20px; line-height: 1.2; margin-top: 4px;
  }
  .contact {
    margin-top: 10px; font-size: 11px; line-height: 1.4; text-align: center; font-style: normal;
  }
  .more-info {
    margin-top: 10px; color: var(--accent-red); font-size: 16px; text-align: center;
  }
  .website { font-size: 17px; text-align: center; margin-top: 2px; }
  .brand {
    position: absolute; right: 0; top: 24px;
    display: flex; align-items: center; gap: 6px;
    font-size: 14px; font-weight: 700; color: var(--ink);
  }
  .brand-dot { width: 20px; height: 20px; border-radius: 50%; background: var(--accent-red); }
</style>
</head>
<body>
  <article class="flyer">
    <span class="edge-band edge-band--left"></span>
    <span class="edge-band edge-band--right"></span>

    <p class="intro">RPT the product of Tol power takes the current power forecast, historical forecast data, historical actual generation data as inputs, crunches the numbers and provides a better probabilistic estimate of Day Ahead Bids.</p>

    <h2 class="section-title">The Power Forecast Map:</h2>

    <div class="forecast-frame">
      <table class="forecast-table">
        <thead>
          <tr>
            <th>hour_flow</th><th>date time</th><th>forecast model 1 in kilowatts</th><th>POWER ACTUAL in kilowatts</th><th>forecast model 2 in kilowatts</th><th>Model 2 error</th><th>percent of error</th>
          </tr>
        </thead>
        <tbody>
          <tr><td>13</td><td class="date">5/14/2012 1:00 PM</td><td>1275.1</td><td>1014.6</td><td>1150.4</td><td>135.8</td><td>13.4</td></tr>
          <tr><td>14</td><td class="date">5/14/2012 2:00 PM</td><td>1183.7</td><td>958.2</td><td>1087.9</td><td>129.7</td><td>13.5</td></tr>
          <tr><td>15</td><td class="date">5/14/2012 3:00 PM</td><td>1092.4</td><td>1021.8</td><td>1040.2</td><td>18.4</td><td>1.8</td></tr>
          <tr><td>16</td><td class="date">5/14/2012 4:00 PM</td><td>986.0</td><td>743.5</td><td>912.6</td><td>169.1</td><td class="alert">22.7</td></tr>
          <tr><td>17</td><td class="date">5/14/2012 5:00 PM</td><td>905.3</td><td>811.9</td><td>860.7</td><td>48.8</td><td>6.0</td></tr>
          <tr><td>18</td><td class="date">5/14/2012 6:00 PM</td><td>842.9</td><td>615.2</td><td>799.3</td><td>184.1</td><td class="alert">29.9</td></tr>
          <tr><td>19</td><td class="date">5/14/2012 7:00 PM</td><td>781.6</td><td>702.4</td><td>744.8</td><td>42.4</td><td>6.0</td></tr>
          <tr><td>20</td><td class="date">5/14/2012 8:00 PM</td><td>735.2</td><td>529.7</td><td>698.1</td><td>168.4</td><td class="alert">31.8</td></tr>
          <tr><td>21</td><td class="date">5/14/2012 9:00 PM</td><td>690.8</td><td>655.3</td><td>671.5</td><td>16.2</td><td>2.5</td></tr>
          <tr><td>22</td><td class="date">5/14/2012 10:00 PM</td><td>648.1</td><td>487.6</td><td>620.9</td><td>133.3</td><td class="alert">27.3</td></tr>
          <tr><td>23</td><td class="date">5/14/2012 11:00 PM</td><td>612.4</td><td>571.0</td><td>590.2</td><td>19.2</td><td>3.4</td></tr>
          <tr><td>24</td><td class="date">5/15/2012 12:00 AM</td><td>588.9</td><td>402.8</td><td>560.7</td><td>157.9</td><td class="alert">39.2</td></tr>
        </tbody>
      </table>
    </div>

    <p class="explainer">What you see above in the picture is what a supply trader sees every day. He sees the hourly forecast in kilo-watt-hour. In some rows both forecast models have over predicted power generation as compared to the actual power generation.</p>

    <section class="offer">
      <div class="dam-photo" role="img" aria-label="Photograph of a hydro power dam with water spilling down its face"></div>
      <div class="offer-copy">
        <p>If you want to improve your supply strategy and revenue, please contact Tol power for arranging a trial. <span class="highlight">The Trial version is free and can be implemented on site or as a cloud solution.</span></p>
        <p class="trial-span">The Trial version has a life span of 2 years.</p>
        <address class="contact">
          Contact Information<br>
          Dinesh Mehra<br>
          Tol power<br>
          Ph: 555.210.4837<br>
          email : dinesh.mehra@tolpowerhub.net
        </address>
        <p class="more-info">FOR MORE INFORMATION VISIT AS AT</p>
        <p class="website">www.tolpowerhub.net</p>
      </div>
      <div class="brand"><span class="brand-dot"></span><span>Tol power</span></div>
    </section>
  </article>
</body>
</html>
```